Plakate für Konzertchor der Liederhalle Brandau
Zielgruppe
Die Liederhalle Brandau und deren Sinfonischer Chor führt chorsinfonische Werke mit Chor- und Orchester und Solisten auf. Weitere Infos unter: https://www.liederhalle-brandau.de/
Aufgabenstellung
Ein frisches und modern gestaltetes Plakat soll für das nächste Konzertprojekt entstehen. Aufgeführt wird:
Wendling As Dur Messe
Tarvik Harbor Mass
Als Gestaltungselement kommen neben Fotos vom Chor, ein Sonnenaufgang, eine Stadt oder eine Darstellung von Sphären/Weltall in Frage. Fotos vom Chor liegen in professioneller Qualität vor.
Neben dem Plakat, können Folgeaufträge für Flyer und Programmheft entstehen.
Konzertchor der Liederhalle Brandau
Kinoensemble Wendhof
Helena Markoudi, Sopran
Wiktoria Lobatsch, Alt
Friedrich Ambacher, Tenor
Udo Kessel, Tenor
Gregor Wiesner, Bass
Ortwin Haller, Dirigent
17.00 Uhr
Lindensaal Brandau

```html
<!DOCTYPE html>
<html lang="de">
<head>
<meta charset="utf-8">
<title>Wendling As Dur Messe · Tarvik Harbor Mass – Liederhalle Brandau</title>
<link rel="stylesheet" href="https://fonts.googleapis.com/css2?family=Bebas+Neue&family=Cormorant+Garamond:wght@500&display=swap">
<style>
  :root {
    --sky-red: #e63b20;
    --sky-orange: #ef7a3a;
    --sky-gold: #f6c27a;
    --sky-pale: #fbe6b4;
    --ridge-peach: #f0a56a;
    --ridge-teal: #7fb3c8;
    --ridge-blue: #2f6fb0;
    --ridge-navy: #223268;
    --night: #1d2347;
    --text: #ffffff;
    --accent: #fcd98b;
  }
  html, body {
    margin: 0;
    padding: 0;
    overflow: hidden;
    background: #ffffff;
  }
  .poster {
    position: relative;
    width: 848px;
    height: 1200px;
    overflow: hidden;
    color: var(--text);
    font-family: "Bebas Neue", "Arial Narrow", sans-serif;
    text-align: center;
  }
  .landscape {
    position: absolute;
    inset: 0;
    background: linear-gradient(180deg,
      var(--sky-red) 0%,
      var(--sky-orange) 17%,
      var(--sky-gold) 31%,
      var(--sky-pale) 40%,
      var(--ridge-peach) 46%,
      var(--ridge-teal) 56%,
      var(--ridge-blue) 67%,
      var(--ridge-navy) 80%,
      var(--night) 100%);
  }
  .brand {
    position: absolute;
    left: 116px;
    top: 62px;
    width: 616px;
    height: 58px;
    box-sizing: border-box;
    border: 1.5px solid var(--text);
    display: flex;
    align-items: center;
    justify-content: center;
    font-family: "Cormorant Garamond", "Times New Roman", serif;
    font-weight: 500;
    font-size: 38px;
    letter-spacing: 2px;
    line-height: 1;
  }
  .line {
    position: absolute;
    left: 0;
    right: 0;
    margin: 0;
    line-height: 1;
    transform: translateY(-50%);
    white-space: nowrap;
  }
  .title { font-size: 100px; letter-spacing: 0.5px; font-weight: 400; }
  .title--first { top: 200px; }
  .title--second { top: 293px; }
  .date { top: 802px; font-size: 78px; word-spacing: 14px; }
  .date .time { margin-left: 40px; }
  .venue { top: 880px; font-size: 78px; }
  .choir { top: 970px; font-size: 48px; color: var(--accent); }
  .credit { font-size: 31px; }
  .orchestra { top: 1022px; }
  .soloists-1 { top: 1058px; }
  .soloists-2 { top: 1093px; }
  .conductor { top: 1148px; }
  .sep { margin: 0 24px; }
</style>
</head>
<body>
  <main class="poster">
    <div class="landscape" role="img" aria-label="Illustration: Sonnenaufgang über hintereinander gestaffelten Bergketten in Orange- und Blautönen"></div>

    <div class="brand">LIEDERHALLE BRANDAU</div>

    <h1 class="line title title--first">Wendling As Dur Messe</h1>
    <h1 class="line title title--second">Tarvik Harbor Mass</h1>

    <p class="line date">SO. 15.10.2023<span class="time">17.00 UHR</span></p>
    <p class="line venue">LINDENSAAL BRANDAU</p>

    <p class="line choir">KONZERTCHOR DER LIEDERHALLE BRANDAU</p>
    <p class="line credit orchestra">KINOENSEMBLE WENDHOF</p>
    <p class="line credit soloists-1">HELENA MARKOUDI, SOPRAN<span class="sep">|</span>WIKTORIA LOBATSCH, ALT</p>
    <p class="line credit soloists-2">FRIEDRICH AMBACHER, TENOR<span class="sep">|</span>UDO KESSEL, TENOR<span class="sep">|</span>GREGOR WIESNER, BASS</p>
    <p class="line credit conductor">ORTWIN HALLER, DIRIGENT</p>
  </main>
</body>
</html>
```